Webdesign für Versicherungsmakler
Zielgruppe
Wir sind ein Versicherungsmakler und wollen unseren Internetauftritt modernisieren. Unsere Zielgruppe sind mittelständische Unternehmen. Wir erstellen neben den Sachversicherungen und der Altersvororge auch versicherungsmathematische Gutachten. Wir beraten, erstellen Angebote und verwalten und betreuen die Versicherungsverträge und Schadenfälle unserer Kunden.
Aufgabenstellung
Es besteht bereits eine Website: https://www.k-und-r.example/. An dieser sollte sich orientiert werden, die Inhalte werden vermutlich in Zukunft Ähnlich bleiben.
Der Aufbau der Website soll modernisiert werden. Das Logo soll erhalten bleiben. Die Seite soll einen modernen, cleanen und dennoch zuverlässigen Eindruck vermitteln.

```html
<!DOCTYPE html>
<html lang="de">
<head>
<meta charset="utf-8">
<title>Kerber &amp; Roth – Versicherungsmakler</title>
<link href="https://fonts.googleapis.com/css2?family=Jost:wght@300;400;500;600&display=swap" rel="stylesheet">
<style>
:root{
  --blue:#003a8c;
  --gold:#c19a35;
  --ink:#1b1b1b;
  --muted:#555;
  --page:#f5f5f5;
  --white:#fff;
  --tint:#eef2f8;
}
*{box-sizing:border-box;margin:0;padding:0}
html,body{width:703px;height:1200px;overflow:hidden}
body{font-family:'Jost',sans-serif;background:var(--page);color:var(--ink);position:relative}
.abs{position:absolute}
/* header */
.site-header{left:0;top:0;width:703px;height:46px;background:var(--white)}
.brand{left:111px;top:12px;display:flex;align-items:center;gap:6px}
.brand-square{width:22px;height:22px;background:var(--blue);border-radius:2px}
.brand-name{font-size:11px;font-weight:400;color:var(--blue);letter-spacing:.5px;line-height:1}
.meta-nav{right:112px;top:10px;display:flex;gap:10px;font-size:5px;color:#333}
.nav-rule{left:344px;top:25px;width:247px;height:1px;background:#e2e2e2}
.main-nav{right:112px;top:31px;display:flex;gap:16px;font-size:6px;font-weight:500;color:var(--ink)}
.main-nav .active{color:var(--blue)}
/* hero */
.hero-panel{left:0;top:46px;width:351px;height:241px;background:var(--blue);border-bottom-right-radius:10px;z-index:2}
.hero-photo{left:345px;top:46px;width:358px;height:241px;background:linear-gradient(120deg,#c9c2b5 0%,#e8e3da 40%,#f0ede6 60%,#b0684a 90%)}
.hero-title{left:111px;top:105px;width:230px;color:var(--white);font-size:15.3px;font-weight:500;line-height:17px;z-index:3}
.hero-text{left:111px;top:167px;width:210px;color:#e6ecf6;font-size:6.6px;line-height:10.3px;font-weight:300;z-index:3}
.btn-gold{left:111px;top:216px;width:108px;height:17px;background:var(--gold);color:var(--white);font-size:6.4px;font-weight:500;border-radius:3px;display:flex;align-items:center;justify-content:center;z-index:3}
.quick-contact{left:680px;top:176px;width:23px;background:var(--white);border-radius:4px 0 0 4px;box-shadow:0 1px 4px rgba(0,0,0,.15);z-index:3}
.quick-item{height:25px;display:flex;flex-direction:column;align-items:center;justify-content:center;font-size:4px;font-weight:500;color:var(--ink);gap:1px}
.quick-item+.quick-item{border-top:1px solid #e5e5e5}
/* feature cards */
.card{background:var(--white);border-radius:7px;overflow:hidden}
.card-photo{position:absolute}
.eyebrow{font-size:6.4px;color:var(--gold);font-weight:400;line-height:9px}
.card-title{font-size:9.8px;font-weight:500;line-height:12.5px;margin-top:5px}
.card-text{font-size:6.2px;font-weight:300;line-height:9px;color:#333;margin-top:6px}
.btn-soft{display:inline-block;margin-top:11px;padding:4px 6px;background:var(--tint);color:var(--blue);font-size:6.7px;font-weight:500;border-radius:3px}
.card-body{position:absolute;white-space:nowrap}
.divider{left:111px;top:603px;width:481px;height:1px;background:#ddd}
/* tiles */
.tile{top:623px;width:117px;height:113px;background:var(--white);border-radius:4px;text-align:center}
.tile-icon{width:36px;height:30px;background:var(--tint);border-radius:3px;margin:16px auto 0;display:flex;align-items:center;justify-content:center}
.tile-title{font-size:8.3px;font-weight:500;margin-top:10px}
.tile-text{font-size:6px;font-weight:300;line-height:9px;color:#333;margin-top:3px}
.tile-arrow{position:absolute;right:10px;bottom:8px}
/* locations */
.loc-photo{left:0;top:768px;width:349px;height:263px;background:linear-gradient(90deg,#6b645c 0%,#958d83 40%,#a9a197 70%,#7e7a70 100%);border-bottom-right-radius:12px}
.loc-panel{left:349px;top:768px;width:354px;height:263px;background:var(--blue)}
.loc-title{left:379px;top:807px;color:var(--white);font-size:14.8px;font-weight:500}
.acc-head{left:379px;width:215px;color:var(--white);font-size:7.3px;font-weight:500;display:flex;justify-content:space-between}
.acc-head span:last-child{color:var(--gold);font-weight:400;font-size:9px;line-height:7px}
.acc-line{left:379px;width:215px;height:1px;background:rgba(255,255,255,.3)}
.loc-info{left:379px;color:var(--white);font-size:6.3px;line-height:10.3px;display:flex;gap:4px}
.loc-info svg{flex:none;margin-top:1px}
/* footer */
.foot-main{left:111px;top:1068px;font-size:8.6px;font-weight:500;line-height:16.2px;color:#333}
.foot-col{font-size:6.2px;line-height:12.4px;color:#666;font-weight:300}
.foot-head{font-size:5.8px;color:var(--blue);font-weight:500;margin-bottom:3px}
.copy{right:110px;top:1154px;font-size:5.6px;color:#888;font-weight:300}
</style>
</head>
<body>

<header class="abs site-header">
  <div class="abs brand"><div class="brand-square"></div><div class="brand-name">KERBER &amp; ROTH</div></div>
  <nav class="abs meta-nav"><span>Privatkunden</span><span>Für Unternehmen</span><span>Downloads</span><span>Karriere</span></nav>
  <div class="abs nav-rule"></div>
  <nav class="abs main-nav"><span class="active">Startseite</span><span>Profil</span><span>Dienstleistungen</span><span>Unternehmen</span><span>Service</span><span>Kontakt</span></nav>
</header>

<section>
  <div class="abs hero-panel"></div>
  <div class="abs hero-photo" role="img" aria-label="Modernes helles Bürogebäude neben rotem Backsteinbau"></div>
  <h1 class="abs hero-title">Beratung mit Weitblick.<br>Ihre Versicherungslösungen<br>in besten Händen.</h1>
  <p class="abs hero-text">Herzlich willkommen bei Kerber &amp; Roth, Ihren unabhängigen<br>Experten für Versicherungsmanagement und betriebliche<br>Altersversorgung!</p>
  <div class="abs btn-gold">Beratungstermin vereinbaren!</div>
  <div class="abs quick-contact">
    <div class="quick-item"><svg width="9" height="9" viewBox="0 0 24 24" fill="none" stroke="#c19a35" stroke-width="2"><path d="M5 3h4l2 5-3 2a11 11 0 0 0 6 6l2-3 5 2v4a2 2 0 0 1-2 2A17 17 0 0 1 3 5a2 2 0 0 1 2-2z"/></svg>Telefon</div>
    <div class="quick-item"><svg width="9" height="9" viewBox="0 0 24 24" fill="none" stroke="#c19a35" stroke-width="2"><rect x="3" y="5" width="18" height="14" rx="1"/><path d="M3 6l9 7 9-7"/></svg>E-Mail</div>
  </div>
</section>

<section>
  <article class="abs card" style="left:111px;top:325px;width:155px;height:256px">
    <div class="card-photo" style="left:0;top:0;width:155px;height:120px;background:linear-gradient(135deg,#c8ccd6,#5c6e8e 55%,#e3e4e8)" role="img" aria-label="Person unterschreibt ein Dokument am Schreibtisch"></div>
    <div class="card-body" style="left:18px;top:135px">
      <div class="eyebrow">Versicherungsmanagement</div>
      <div class="card-title">Smarte Lösungen für<br>Ihren Bedarf</div>
      <div class="card-text">„Gut versichert“ beginnt mit kluger<br>Analyse &amp; langfristiger Betreuung.</div>
      <div class="btn-soft">Mehr erfahren</div>
    </div>
  </article>
  <article class="abs card" style="left:274px;top:325px;width:318px;height:120px">
    <div class="card-photo" style="left:0;top:0;width:162px;height:120px;background:linear-gradient(135deg,#9a8a78,#d7c9b4 50%,#7a6a58)" role="img" aria-label="Älteres Paar plant gemeinsam am Tablet"></div>
    <div class="card-body" style="left:178px;top:12px">
      <div class="eyebrow">Altersvorsorge</div>
      <div class="card-title">Altersvorsorge, die zu<br>Ihnen passt</div>
      <div class="card-text">Wir beraten, optimieren und verwalten —<br>individuell &amp; zuverlässig.</div>
      <div class="btn-soft">Mehr erfahren</div>
    </div>
  </article>
  <article class="abs card" style="left:274px;top:452px;width:318px;height:129px">
    <div class="card-photo" style="left:0;top:0;width:162px;height:129px;background:linear-gradient(135deg,#3b4c6e,#b9c0cc 50%,#e6e3df)" role="img" aria-label="Hand mit Stift am Taschenrechner über Diagrammen"></div>
    <div class="card-body" style="left:178px;top:12px">
      <div class="eyebrow">Versicherungsmathematische<br>Gutachten</div>
      <div class="card-title">Zukunft planen,<br>Sicherheit gewinnen.</div>
      <div class="card-text">Klug vorsorgen, präzise kalkulieren.<br>Wir machen Ihre Zukunft berechenbar!</div>
      <div class="btn-soft">Mehr erfahren</div>
    </div>
  </article>
  <div class="abs divider"></div>
</section>

<section>
  <a class="abs tile" style="left:110px">
    <div class="tile-icon"><svg width="16" height="14"><rect x="1" y="1" width="14" height="12" rx="2" fill="none" stroke="#003a8c" stroke-width="1.6"/></svg></div>
    <div class="tile-title">Profil</div>
    <div class="tile-text">Lorem ipsum dolor sit amet,<br>consetetur sadipscing</div>
    <svg class="tile-arrow" width="9" height="6" viewBox="0 0 9 6"><path d="M0 3h8M5.5 .5L8 3 5.5 5.5" fill="none" stroke="#c19a35"/></svg>
  </a>
  <a class="abs tile" style="left:232px">
    <div class="tile-icon"><svg width="16" height="16" viewBox="0 0 16 16"><path d="M8 1l7 7-7 7-7-7z" fill="none" stroke="#003a8c" stroke-width="1.8"/><path d="M5 8l3-3M7 10l3-3" stroke="#003a8c" stroke-width="1.3"/></svg></div>
    <div class="tile-title">Dienstleistungen</div>
    <div class="tile-text">Lorem ipsum dolor sit amet,<br>consetetur sadipscing</div>
    <svg class="tile-arrow" width="9" height="6" viewBox="0 0 9 6"><path d="M0 3h8M5.5 .5L8 3 5.5 5.5" fill="none" stroke="#c19a35"/></svg>
  </a>
  <a class="abs tile" style="left:354px">
    <div class="tile-icon"><svg width="20" height="12" viewBox="0 0 20 12" fill="#003a8c"><circle cx="10" cy="3" r="2.5"/><circle cx="4" cy="4.5" r="2"/><circle cx="16" cy="4.5" r="2"/><path d="M6 12a4 4 0 0 1 8 0z"/><path d="M0 12a3.5 3.5 0 0 1 6-2.5V12zM20 12a3.5 3.5 0 0 0-6-2.5V12z"/></svg></div>
    <div class="tile-title">Unternehmen</div>
    <div class="tile-text">Lorem ipsum dolor sit amet,<br>consetetur sadipscing</div>
    <svg class="tile-arrow" width="9" height="6" viewBox="0 0 9 6"><path d="M0 3h8M5.5 .5L8 3 5.5 5.5" fill="none" stroke="#c19a35"/></svg>
  </a>
  <a class="abs tile" style="left:476px">
    <div class="tile-icon"><svg width="18" height="20" viewBox="0 0 18 20"><path d="M9 1a8 8 0 1 1-3 15.4L9 19l0-2.1" fill="none" stroke="#003a8c" stroke-width="1.8"/><text x="9" y="13" text-anchor="middle" font-family="Jost,sans-serif" font-size="10" font-weight="600" fill="#003a8c">?</text></svg></div>
    <div class="tile-title">Service</div>
    <div class="tile-text">Lorem ipsum dolor sit amet,<br>consetetur sadipscing</div>
    <svg class="tile-arrow" width="9" height="6" viewBox="0 0 9 6"><path d="M0 3h8M5.5 .5L8 3 5.5 5.5" fill="none" stroke="#c19a35"/></svg>
  </a>
</section>

<section>
  <div class="abs loc-photo" role="img" aria-label="Unscharfer Blick in den Empfangsbereich mit Firmenschild an der Glaswand"></div>
  <div class="abs loc-panel"></div>
  <h2 class="abs loc-title">Unsere Standorte</h2>
  <div class="abs acc-head" style="top:838px"><span>Büro Potsdam</span><span>–</span></div>
  <div class="abs loc-info" style="top:855px"><svg width="7" height="9" viewBox="0 0 12 16"><path d="M6 15S1 9 1 6a5 5 0 0 1 10 0c0 3-5 9-5 9z" fill="none" stroke="#c19a35" stroke-width="1.5"/><circle cx="6" cy="6" r="1.8" fill="none" stroke="#c19a35" stroke-width="1.3"/></svg><div>Kerber &amp; Roth GmbH<br>Lindenallee 8<br>14999 Potsdam</div></div>
  <div class="abs loc-info" style="top:896px"><svg width="8" height="8" viewBox="0 0 24 24" fill="none" stroke="#c19a35" stroke-width="2"><path d="M5 3h4l2 5-3 2a11 11 0 0 0 6 6l2-3 5 2v4a2 2 0 0 1-2 2A17 17 0 0 1 3 5a2 2 0 0 1 2-2z"/></svg><div>0300 / 5 40 12 - 0</div></div>
  <div class="abs loc-info" style="top:906px"><svg width="8" height="8" viewBox="0 0 16 16" fill="none" stroke="#c19a35" stroke-width="1.4"><rect x="1" y="6" width="14" height="8" rx="1"/><rect x="4" y="2" width="8" height="4"/></svg><div>0300 / 5 40 12 - 10</div></div>
  <div class="abs loc-info" style="top:927px"><svg width="8" height="8" viewBox="0 0 24 24" fill="none" stroke="#c19a35" stroke-width="2"><rect x="3" y="5" width="18" height="14" rx="1"/><path d="M3 6l9 7 9-7"/></svg><div>info@k-und-r.example</div></div>
  <div class="abs loc-info" style="top:937px"><svg width="8" height="8" viewBox="0 0 16 16" fill="none" stroke="#c19a35" stroke-width="1.3"><circle cx="8" cy="8" r="6.5"/><path d="M1.5 8h13M8 1.5c-3 3.5-3 9.5 0 13M8 1.5c3 3.5 3 9.5 0 13"/></svg><div>k-und-r.example</div></div>
  <div class="abs acc-line" style="top:958px"></div>
  <div class="abs acc-head" style="top:963px"><span>Büro Werder (Postanschrift</span><span>+</span></div>
  <div class="abs acc-line" style="top:978px"></div>
  <div class="abs acc-head" style="top:983px"><span>Büro Hannover</span><span>+</span></div>
</section>

<footer>
  <nav class="abs foot-main">Startseite<br>Profil<br>Dienstleistungen<br>Unternehmen<br>Service<br>Kontakt</nav>
  <div class="abs foot-col" style="left:305px;top:1062px">Für Privatkunden<br>Für Unternehmen<br>Karriere
    <div class="foot-head" style="margin-top:10px">Hilfe &amp; Service</div>Kontaktformular<br>Downloads</div>
  <div class="abs foot-col" style="left:427px;top:1065px"><div class="foot-head">Rechtliches</div>Impressum<br>Datenschutz<br>AGB</div>
  <div class="abs foot-col" style="left:549px;top:1065px"><div class="foot-head">Social Media</div><span style="display:inline-block;width:6px;height:6px;background:var(--gold);margin-right:4px;vertical-align:-0.5px"></span>Kontaktnetz</div>
  <div class="abs copy">2025 © Kerber &amp; Roth GmbH</div>
</footer>

</body>
</html>
```